Heronby Mortgage Capital Business Card

We need a business card design for our mortgage servicing company. In addition to servicing the loans of homeowners, we help homeowners with purchasing their homes and any mortgage refinancing. We would like to see designs that use the colors in the logo attached below (gold-ish yellow and navy blue), and any other design you deem fit! The design should communicate a simpler life with smart mortgages provided by Heronby.

```html
<!DOCTYPE html>
<html lang="en">
<head>
<meta charset="utf-8">
<title>Heronby Mortgage Capital – Business Card</title>
<link rel="stylesheet" href="https://fonts.googleapis.com/css2?family=Montserrat:wght@400;500;700&display=swap">
<style>
  :root {
    --navy: #27214f;
    --navy-deep: #1b1745;
    --gold: #e0b13f;
    --white: #ffffff;
    --backdrop: #ececec;
    --ink: #1f1c3a;
  }
  * { margin: 0; padding: 0; box-sizing: border-box; }
  html, body {
    width: 1200px; height: 1200px; overflow: hidden;
    background: var(--backdrop);
    font-family: "Montserrat", sans-serif;
  }
  .canvas { position: relative; width: 1200px; height: 1200px; }
  .card {
    position: absolute; left: 181px; width: 838px; height: 494px;
    background: var(--white); overflow: hidden;
  }
  .card--front { top: 72px; }
  .card--back { top: 634px; }
  .card__shapes { position: absolute; inset: 0; width: 100%; height: 100%; }

  .brand {
    position: absolute; display: flex; align-items: center; gap: 14px;
    transform: translate(-50%, -50%);
    color: var(--navy); font-weight: 700; white-space: nowrap;
  }
  .brand__dot { width: 22px; height: 22px; border-radius: 50%; background: var(--gold); flex: none; }
  .brand--front { left: 269px; top: 196px; font-size: 34px; }
  .brand--back { left: 419px; top: 198px; font-size: 46px; }

  .name-banner {
    position: absolute; right: 0; top: 54px; width: 382px; height: 78px;
    background: var(--navy); color: var(--white); text-align: right;
    padding: 12px 48px 0 0;
  }
  .name-banner__name { font-size: 28px; font-weight: 700; letter-spacing: 0.5px; line-height: 1.1; }
  .name-banner__role { font-size: 19px; font-weight: 400; line-height: 1.3; }

  .contact { position: absolute; right: 42px; top: 264px; list-style: none; color: var(--ink); }
  .contact__item {
    display: flex; justify-content: flex-end; align-items: center; gap: 16px;
    font-size: 20px; line-height: 32px;
  }
  .contact__item--address { margin-top: 24px; align-items: flex-start; }
  .contact__lines { text-align: right; line-height: 28px; }
  .contact__icon { width: 16px; height: 16px; flex: none; fill: var(--ink); }
  .contact__item--address .contact__icon { margin-top: 6px; }

  .web-ribbon {
    position: absolute; left: 134px; top: 372px; width: 570px; height: 59px;
    display: flex; align-items: center; justify-content: center;
    color: var(--white); font-size: 22px; letter-spacing: 4px;
  }
</style>
</head>
<body>
<main class="canvas">

  <section class="card card--front" aria-label="Business card front">
    <svg class="card__shapes" viewBox="0 0 670 395" preserveAspectRatio="none" aria-hidden="true">
      <polygon fill="var(--gold)" points="615,0 670,0 670,395 0,395 0,239 195,320"/>
      <polygon fill="var(--navy-deep)" points="390,105 485,105 455,157"/>
    </svg>

    <div class="brand brand--front"><span class="brand__dot"></span>Heronby Mortgage</div>

    <div class="name-banner">
      <p class="name-banner__name">DELIA VARNHOLT</p>
      <p class="name-banner__role">Owner</p>
    </div>

    <ul class="contact">
      <li class="contact__item">5550 184 372
        <svg class="contact__icon" viewBox="0 0 16 16"><path d="M3.5 1.5l2.5 2.8-1.3 1.9c.9 2 2.6 3.7 4.6 4.6l1.9-1.3 2.8 2.5-1.4 2.2C7 14 2 9 1.3 2.9z"/></svg>
      </li>
      <li class="contact__item">delia@heronbymortgage.com
        <svg class="contact__icon" viewBox="0 0 16 16"><path d="M1 3h14v10H1zM2 4.2v.5l6 4.3 6-4.3v-.5z"/></svg>
      </li>
      <li class="contact__item">www.heronbymortgage.com
        <svg class="contact__icon" viewBox="0 0 16 16"><path d="M8 1a7 7 0 100 14A7 7 0 008 1zm0 1.6c.9 1 1.5 2.6 1.6 4.6H6.4C6.5 5.2 7.1 3.6 8 2.6zM2.7 8.8h2.1c.1 1.6.5 3 1.1 4A5.5 5.5 0 012.7 8.8zm0-1.6a5.5 5.5 0 013.2-4c-.6 1-1 2.4-1.1 4zm5.3 6.2c-.9-1-1.5-2.6-1.6-4.6h3.2c-.1 2-.7 3.6-1.6 4.6zm2.1-.6c.6-1 1-2.4 1.1-4h2.1a5.5 5.5 0 01-3.2 4zm1.1-5.6c-.1-1.6-.5-3-1.1-4a5.5 5.5 0 013.2 4z"/></svg>
      </li>
      <li class="contact__item contact__item--address">
        <span class="contact__lines">2400 W Harbor View Dr, Suite 4<br>Tempe, AZ 85281</span>
        <svg class="contact__icon" viewBox="0 0 16 16"><path d="M8 1a4 4 0 00-4 4c0 3 4 7 4 7s4-4 4-7a4 4 0 00-4-4zm0 5.5A1.5 1.5 0 118 3.5a1.5 1.5 0 010 3zM2 13h12v2H2z"/></svg>
      </li>
    </ul>
  </section>

  <section class="card card--back" aria-label="Business card back">
    <svg class="card__shapes" viewBox="0 0 670 395" preserveAspectRatio="none" aria-hidden="true">
      <polygon fill="var(--navy-deep)" points="107,345 155,345 155,393"/>
      <polygon fill="var(--navy-deep)" points="515,345 563,345 515,393"/>
      <rect fill="var(--navy)" x="107" y="298" width="456" height="47"/>
    </svg>

    <div class="brand brand--back"><span class="brand__dot"></span>Heronby Mortgage</div>

    <p class="web-ribbon">www.heronbymortgage.com</p>
  </section>

</main>
</body>
</html>
```